TARVEL RENOVATIONS AND CUSTOM BUILDS

5pages:
Home/ who we are , services offered, why us,
recent projects/ gallery , contact us

Industry/Entity Type

Design, renovations, project management

Coding

Coded - Design and coding required

Number of Pages Required

5+ page

Requirements
Should not have
• Too many colours

```html
<!DOCTYPE html>
<html lang="en">
<head>
<meta charset="utf-8">
<title>Tarvel Renovations and Custom Builds</title>
<link href="https://fonts.googleapis.com/css2?family=Poppins:ital,wght@0,300;0,400;0,500;0,600;0,700;1,400&display=swap" rel="stylesheet">
<style>
:root{
  --navy:#2d3e5c;
  --green:#7cb83a;
  --ink:#1f1f1f;
  --text:#555a60;
  --dark:#262626;
  --field:#3a3a3a;
  --light:#f1f2f3;
  --white:#ffffff;
}
*{box-sizing:border-box;margin:0;padding:0}
html,body{width:1200px;height:5059px;overflow:hidden}
body{position:relative;font-family:'Poppins',sans-serif;color:var(--ink);background:var(--white)}
.abs{position:absolute}
.center{left:0;width:1200px;text-align:center}

/* header */
.brand{display:flex;align-items:center;gap:10px;font-weight:600;font-size:14px;line-height:20px;color:var(--navy)}
.brand .mark{flex:none;width:30px;height:30px;background:var(--navy)}
.footer-brand{color:var(--white);font-size:15px;line-height:22px;width:230px}
.footer-brand .mark{background:var(--white)}
.contact-top{top:20px;display:flex;align-items:center;gap:10px}
.contact-top .ico{width:38px;height:38px;border:2px solid var(--navy);border-radius:50%;display:flex;align-items:center;justify-content:center}
.contact-top small{display:block;font-size:12px;color:var(--text)}
.contact-top b{font-size:15px;font-weight:500;color:var(--navy)}
.nav{top:88px;left:384px;display:flex;gap:40px;font-size:14px;font-weight:500;color:var(--ink)}
.nav .on{color:var(--green)}

/* hero */
.hero-photo{top:130px;left:0;width:1200px;height:692px;background:linear-gradient(120deg,#c9c4bd 0%,#9c9186 40%,#6b5d51 70%,#b7b1aa 100%);clip-path:polygon(0 0,100% 0,100% 84%,50% 100%,0 84%)}
.hero-title{top:355px;font-size:34px;font-weight:600;color:var(--white)}
.hero-text{top:412px;font-size:15px;line-height:28px;color:var(--white)}
.btn{display:inline-block;background:var(--green);color:var(--white);font-size:13px;font-weight:600;padding:0 28px;line-height:36px}
.arrow{width:34px;height:60px}
.dots{top:764px;left:526px;display:flex;gap:12px}
.dots i{display:block;width:40px;height:3px;background:rgba(255,255,255,.5)}
.dots i.on{background:var(--white)}

/* welcome */
.h2{font-size:32px;font-weight:400;line-height:40px;color:var(--ink)}
.h2 b{font-weight:600}
.para{font-size:14px;line-height:32px;color:var(--text)}
.card{width:316px}
.card .photo{height:248px;border-radius:8px}
.card .box{position:absolute;top:170px;left:18px;width:283px;height:220px;background:var(--white);border-radius:10px;box-shadow:0 4px 14px rgba(0,0,0,.12);text-align:center;padding-top:22px}
.card h3{font-size:21px;font-weight:600;line-height:24px;color:var(--ink)}
.card p{font-size:13px;line-height:24px;color:var(--text);margin-top:14px;padding:0 16px}
.card a{display:inline-block;margin-top:6px;font-size:14px;font-weight:600;color:var(--green);text-decoration:underline}

/* why choose */
.why-photo{top:1650px;left:0;width:1200px;height:575px;background:linear-gradient(90deg,#5a4636 0%,#2d3440 35%,#2c3a4b 65%,#3b4a3c 100%);clip-path:polygon(0 105px,50% 0,100% 105px,100% 100%,0 100%)}
.why-shade{top:1650px;left:0;width:1200px;height:575px;background:rgba(20,28,40,.45);clip-path:polygon(0 105px,50% 0,100% 105px,100% 100%,0 100%)}

/* ring */
.rp-title{font-size:32px;line-height:40px;color:var(--ink)}
.rp-title b{font-weight:600}
.underline{width:60px;height:3px;background:var(--navy)}
.feat{width:260px}
.feat h4{font-size:15px;font-weight:600;color:var(--ink);margin-bottom:4px}
.feat p{font-size:13px;line-height:25px;color:var(--text)}
.feat.l{text-align:right}
.ring-ico{width:86px;height:86px;border-radius:50%;background:var(--navy);display:flex;align-items:center;justify-content:center}

/* stats */
.stats{top:3005px;left:0;width:1200px;height:217px;background:var(--navy)}
.stat{top:60px;width:240px;text-align:center;color:var(--white)}
.stat b{display:block;font-size:30px;font-weight:500;line-height:38px}
.stat span{display:block;font-size:21px;line-height:27px}
.vline{top:75px;width:1px;height:70px;background:rgba(255,255,255,.35)}

/* gallery */
.gallery{top:3222px;left:0;width:1200px;height:751px;background:var(--light)}
.tile{width:240px;height:244px}

/* reviews */
.quote-mark{font-size:92px;font-weight:700;color:#b9c0cc;line-height:1}
.review{font-size:17px;font-style:italic;line-height:37px;color:var(--ink)}
.reviewer{font-size:19px;font-weight:600;color:var(--ink)}

/* footer */
.footer{top:4470px;left:0;width:1200px;height:589px;background:var(--dark);clip-path:polygon(0 112px,50% 0,100% 112px,100% 100%,0 100%)}
.f-head{font-size:18px;font-weight:500;color:var(--white);letter-spacing:.5px}
.f-item{display:flex;gap:12px;font-size:14px;line-height:19px;color:var(--white)}
.f-item .ico{flex:none;width:34px;height:34px;border:1.5px solid var(--white);border-radius:50%;display:flex;align-items:center;justify-content:center}
.field{width:293px;height:38px;background:var(--field);font-size:12px;color:#d8d8d8;padding:10px 14px}
.links{font-size:14px;line-height:36px;color:var(--white);list-style:none}
.social{width:36px;height:36px;border:1.5px solid var(--white);border-radius:50%}
.copy{top:5015px;font-size:13px;color:#d8d8d8}
</style>
</head>
<body>

<!-- header -->
<div class="abs brand" style="left:98px;top:62px"><span class="mark"></span><span>TARVEL RENOVATIONS AND CUSTOM BUILDS</span></div>
<div class="abs contact-top" style="left:500px">
  <div class="ico"><svg width="18" height="18" viewBox="0 0 24 24"><path d="M6.6 10.8a15 15 0 0 0 6.6 6.6l2.2-2.2a1 1 0 0 1 1-.25 11 11 0 0 0 3.6.6 1 1 0 0 1 1 1V20a1 1 0 0 1-1 1A17 17 0 0 1 3 4a1 1 0 0 1 1-1h3.5a1 1 0 0 1 1 1c0 1.25.2 2.45.6 3.6a1 1 0 0 1-.25 1z" fill="#2d3e5c"/></svg></div>
  <div><small>Call Us</small><b>(555) 014-2280</b></div>
</div>
<div class="abs contact-top" style="left:700px">
  <div class="ico"><svg width="18" height="14" viewBox="0 0 24 18"><rect x="1" y="1" width="22" height="16" rx="2" fill="none" stroke="#2d3e5c" stroke-width="2"/><path d="M1 2l11 8 11-8" fill="none" stroke="#2d3e5c" stroke-width="2"/></svg></div>
  <div><small>Email Us</small><b>info@tarvelrenovations.com</b></div>
</div>
<nav class="abs nav">
  <span class="on">HOME</span><span>WHO WE ARE</span><span>SERVICES OFFERED</span><span>WHY US</span><span>GALLERY</span><span>CONTACT US</span>
</nav>

<!-- hero -->
<svg class="abs" style="top:700px;left:0" width="1200" height="140" viewBox="0 0 1200 140"><polygon points="0,10 600,120 1200,10 1200,30 600,136 0,30" fill="#7cb83a"/></svg>
<div class="abs hero-photo" role="img" aria-label="Bright modern kitchen with white cabinets, a wooden island and pendant lights"></div>
<div class="abs center hero-title">TARVEL RENOVATIONS &amp; CUSTOM BUILDS</div>
<div class="abs center hero-text">Lorem ipsum dolor sit amet, consectetur adipiscing elit, sed do eiusmod tempor<br>incididunt ut labore et dolore magna aliqua.</div>
<div class="abs center" style="top:490px"><span class="btn">GET STARTED</span></div>
<svg class="abs arrow" style="left:52px;top:415px" viewBox="0 0 34 60"><path d="M30 4L4 30l26 26" fill="none" stroke="#fff" stroke-width="2"/></svg>
<svg class="abs arrow" style="left:1114px;top:415px" viewBox="0 0 34 60"><path d="M4 4l26 26L4 56" fill="none" stroke="#fff" stroke-width="2"/></svg>
<div class="abs dots"><i></i><i class="on"></i><i></i></div>

<!-- welcome -->
<div class="abs center h2" style="top:905px">WELCOME TO<br><b>TARVEL RENOVATIONS &amp; CUSTOM BUILDS</b></div>
<p class="abs para" style="top:1004px;left:130px;width:940px;text-align:center">At quas molestias excepturi sint occaecati cupiditate non provident, similique sunt ilpa qui officia deserunt mollitia animi, id est laborum et dolorum fuga. Et harum quidem rerum facilis est et expedita distinctio. Nam libero tempore, cum soluta nobis est eligendi optio cumque nihil impedit qinus id quod maxime placeat facere possimus, omnis voluptas assumenda est, omnis dolor repellendus. Temporibus autem quibusdam et aut</p>

<div class="abs card" style="left:98px;top:1167px">
  <div class="photo" role="img" aria-label="Builder in a hard hat in front of a timber roof frame" style="background:linear-gradient(160deg,#9bb7d4,#c98a5a 60%,#7a5a3f)"></div>
  <div class="box"><h3>Custom Home<br>Builder</h3><p>Lorem ipsum dolor sit a consectetur adipiscing elit, seo eiusmod tempor incididunt ut labore et</p><a>LEARN MORE</a></div>
</div>
<div class="abs card" style="left:442px;top:1167px">
  <div class="photo" role="img" aria-label="Renovated open living and dining room" style="background:linear-gradient(160deg,#e9e8e5,#b8b5b0 60%,#8d8a86)"></div>
  <div class="box"><h3>Whole House<br>Remodels</h3><p>Lorem ipsum dolor sit a consectetur adipiscing elit, seo eiusmod tempor incididunt ut labore et</p><a>LEARN MORE</a></div>
</div>
<div class="abs card" style="left:784px;top:1167px">
  <div class="photo" role="img" aria-label="Kitchen with light wooden cabinets and a window" style="background:linear-gradient(160deg,#e2d2bc,#c4a886 60%,#9c8064)"></div>
  <div class="box"><h3>Kitchen<br>Remodels</h3><p>Lorem ipsum dolor sit a consectetur adipiscing elit, seo eiusmod tempor incididunt ut labore et</p><a>LEARN MORE</a></div>
</div>

<!-- why choose -->
<svg class="abs" style="top:1640px;left:0" width="1200" height="120" viewBox="0 0 1200 120"><polygon points="0,100 600,0 1200,100 1200,125 600,12 0,115" fill="#7cb83a"/></svg>
<div class="abs why-photo" role="img" aria-label="Dark modern living room with a fireplace, stairs and leather chairs"></div>
<div class="abs why-shade"></div>
<div class="abs center h2" style="top:1795px;color:#fff">WHY CHOOSE<br><b>TARVEL RENOVATIONS &amp; CUSTOM BUILDS</b></div>
<p class="abs para" style="top:1893px;left:205px;width:790px;text-align:center;color:#fff;font-size:16px;line-height:34px">At quas molestias excepturi sint occaecati cupiditate non provident, similique sunt ilpa qui officia deserunt mollitia animi, id est laborum et dolorum fuga. Et harum quidem rerum facilis est et expedita distinctio. Nam libero tempore, cum soluta nobis</p>
<div class="abs center" style="top:2025px"><span class="btn">LEARN MORE</span></div>

<!-- recent projects ring -->
<div class="abs center rp-title" style="top:2298px">RECENT <b>PROJECTS</b></div>
<div class="abs underline" style="top:2342px;left:570px"></div>
<p class="abs para" style="top:2370px;left:150px;width:900px;text-align:center;line-height:30px">At quas molestias excepturi sint occaecati cupiditate non provident, similique sunt ilpa qui officia deserunt mollitia animi, id est laborum et dolorum fuga. Et harum quidem rerum facilis est et expedita distinctio.</p>

<svg class="abs" style="top:2484px;left:394px" width="412" height="412" viewBox="0 0 412 412"><circle cx="206" cy="206" r="204" fill="none" stroke="#2d3e5c" stroke-width="1.5"/></svg>

<div class="abs ring-ico" style="left:409px;top:2497px"><svg width="44" height="44" viewBox="0 0 44 44" fill="none" stroke="#fff" stroke-width="2"><path d="M4 22L22 6l18 16M9 18v20h26V18"/><path d="M15 32l14-14M15 18l14 14"/></svg></div>
<div class="abs ring-ico" style="left:703px;top:2497px"><svg width="44" height="44" viewBox="0 0 44 44" fill="none" stroke="#fff" stroke-width="2"><rect x="7" y="8" width="30" height="28"/><path d="M7 18h30M7 27h30M17 8v28M27 8v28"/></svg></div>
<div class="abs ring-ico" style="left:346px;top:2654px"><svg width="44" height="44" viewBox="0 0 44 44" fill="none" stroke="#fff" stroke-width="2"><rect x="8" y="8" width="18" height="10" rx="2"/><path d="M26 13h6v10H18v6M16 29h4v10h-4z"/></svg></div>
<div class="abs ring-ico" style="left:766px;top:2654px"><svg width="44" height="44" viewBox="0 0 44 44" fill="none" stroke="#fff" stroke-width="2"><path d="M4 22L22 6l18 16M9 18v20h26V18"/><circle cx="22" cy="27" r="6"/></svg></div>
<div class="abs ring-ico" style="left:409px;top:2811px"><svg width="44" height="44" viewBox="0 0 44 44" fill="none" stroke="#fff" stroke-width="2"><rect x="8" y="14" width="28" height="22"/><path d="M8 22h28M14 28h16M16 6v4M22 6v4M28 6v4"/></svg></div>
<div class="abs ring-ico" style="left:703px;top:2811px"><svg width="44" height="44" viewBox="0 0 44 44" fill="none" stroke="#fff" stroke-width="2"><rect x="10" y="6" width="24" height="32"/><path d="M15 14h14M15 20h14M15 26h8"/></svg></div>

<div class="abs feat l" style="left:134px;top:2490px"><h4>Finibus Bonorum et Malo</h4><p>Lorem ip dolr it amet, consectetur adipicing ed do eiusmod tempor incididunt ut labore</p></div>
<div class="abs feat" style="left:804px;top:2490px"><h4>Finibus Bonorum et Malo</h4><p>Lorem ip dolr it amet, consectetur adipicing ed do eiusmod tempor incididunt ut labore</p></div>
<div class="abs feat l" style="left:72px;top:2647px"><h4>Finibus Bonorum et Malo</h4><p>Lorem ip dolr it amet, consectetur adipicing ed do eiusmod tempor incididunt ut labore</p></div>
<div class="abs feat" style="left:866px;top:2647px"><h4>Finibus Bonorum et Malo</h4><p>Lorem ip dolr it amet, consectetur adipicing ed do eiusmod tempor incididunt ut labore</p></div>
<div class="abs feat l" style="left:134px;top:2804px"><h4>Finibus Bonorum et Malo</h4><p>Lorem ip dolr it amet, consectetur adipicing ed do eiusmod tempor incididunt ut labore</p></div>
<div class="abs feat" style="left:800px;top:2804px"><h4>Finibus Bonorum et Malo</h4><p>Lorem ip dolr it amet, consectetur adipicing ed do eiusmod tempor incididunt ut labore</p></div>

<!-- stats -->
<div class="abs stats">
  <div class="abs stat" style="left:68px"><b>2023</b><span>Year<br>Established</span></div>
  <div class="abs vline" style="left:330px"></div>
  <div class="abs stat" style="left:352px"><b>206</b><span>Projects<br>Completed</span></div>
  <div class="abs vline" style="left:612px"></div>
  <div class="abs stat" style="left:642px"><b>870</b><span>Business<br>Environment</span></div>
  <div class="abs vline" style="left:910px"></div>
  <div class="abs stat" style="left:912px"><b>26</b><span>Awards<br>Won</span></div>
</div>

<!-- gallery -->
<div class="abs gallery"></div>
<div class="abs center rp-title" style="top:3309px">RECENT <b>PROJECTS</b></div>
<div class="abs tile" style="left:98px;top:3384px;background:linear-gradient(150deg,#d9d2c8,#8a6a4c)" role="img" aria-label="Kitchen under construction with wooden cabinets"></div>
<div class="abs tile" style="left:354px;top:3384px;background:linear-gradient(150deg,#c96a4a,#a05a3e 50%,#d9d4cc)" role="img" aria-label="Brick cottage with red tile roof"></div>
<div class="abs tile" style="left:607px;top:3384px;background:linear-gradient(150deg,#b8a89a,#9c5a44 60%,#8c8884)" role="img" aria-label="Brick house extension with building materials"></div>
<div class="abs tile" style="left:860px;top:3384px;background:linear-gradient(180deg,#a9c6dd,#5d6a5a 50%,#5e8a3a)" role="img" aria-label="Single storey house with front lawn"></div>
<div class="abs tile" style="left:98px;top:3640px;background:linear-gradient(150deg,#e4e2de,#bdb8b1)" role="img" aria-label="Tiled walk-in shower"></div>
<div class="abs tile" style="left:354px;top:3640px;background:linear-gradient(150deg,#3a3430,#8a4a2e 50%,#2a2a2a)" role="img" aria-label="Timber and steel roof structure"></div>
<div class="abs tile" style="left:607px;top:3640px;background:linear-gradient(150deg,#d8cfc4,#9a8c7e)" role="img" aria-label="Bedroom with upholstered bench and armchair"></div>
<div class="abs tile" style="left:860px;top:3640px;background:linear-gradient(150deg,#3a2a20,#7a5a40 50%,#2a2a2a)" role="img" aria-label="Interior with reclaimed wood feature wall"></div>

<!-- reviews -->
<div class="abs center h2" style="top:4045px">TARVEL RENOVATIONS<br><b>REVIEWS</b></div>
<div class="abs center quote-mark" style="top:4140px">&ldquo;</div>
<p class="abs review" style="top:4203px;left:190px;width:820px;text-align:center">Lorem ipsum dolor sit amet, consectetur adipiscing elit, sed do eiusmod tpor incididunt ut labore et dolore magna aliqua. Quis ipsum suspendisse ultricevida. Risus commodo viverra maecenas accumsan lacus vel facilisis. Lorem ipsum dor sit amet, consectetur adipiscing elit, sed do eiusmod tempor incididunt</p>
<div class="abs center reviewer" style="top:4364px">Dana Whitfield</div>
<svg class="abs" style="left:118px;top:4244px" width="26" height="46" viewBox="0 0 26 46"><path d="M23 2L3 23l20 21" fill="none" stroke="#1f1f1f" stroke-width="2"/></svg>
<svg class="abs" style="left:1056px;top:4244px" width="26" height="46" viewBox="0 0 26 46"><path d="M3 2l20 21L3 44" fill="none" stroke="#1f1f1f" stroke-width="2"/></svg>

<!-- footer -->
<svg class="abs" style="top:4464px;left:0" width="1200" height="130" viewBox="0 0 1200 130"><polygon points="0,112 600,0 1200,112 1200,120 600,8 0,120" fill="#7cb83a"/></svg>
<div class="abs footer"></div>

<div class="abs brand footer-brand" style="left:98px;top:4660px"><span class="mark"></span><span>TARVEL RENOVATIONS AND CUSTOM BUILDS</span></div>
<div class="abs" style="left:104px;top:4748px;display:flex;gap:10px">
  <div class="social"></div><div class="social"></div><div class="social"></div><div class="social"></div>
</div>

<div class="abs f-head" style="left:346px;top:4620px">CONTACT US</div>
<div class="abs f-item" style="left:346px;top:4665px">
  <div class="ico"><svg width="14" height="18" viewBox="0 0 14 18"><path d="M7 1a6 6 0 0 1 6 6c0 4.5-6 10-6 10S1 11.5 1 7a6 6 0 0 1 6-6z" fill="none" stroke="#fff" stroke-width="1.6"/><circle cx="7" cy="7" r="2" fill="#fff"/></svg></div>
  <div>48 Harbor Lane<br>Springdale USA</div>
</div>
<div class="abs f-item" style="left:346px;top:4734px">
  <div class="ico"><svg width="16" height="16" viewBox="0 0 24 24"><path d="M6.6 10.8a15 15 0 0 0 6.6 6.6l2.2-2.2a1 1 0 0 1 1-.25 11 11 0 0 0 3.6.6 1 1 0 0 1 1 1V20a1 1 0 0 1-1 1A17 17 0 0 1 3 4a1 1 0 0 1 1-1h3.5a1 1 0 0 1 1 1c0 1.25.2 2.45.6 3.6a1 1 0 0 1-.25 1z" fill="#fff"/></svg></div>
  <div>Phone:<br>(555) 014-2280</div>
</div>
<div class="abs f-item" style="left:346px;top:4808px">
  <div class="ico"><svg width="16" height="12" viewBox="0 0 24 18"><rect x="1" y="1" width="22" height="16" rx="2" fill="none" stroke="#fff" stroke-width="2"/><path d="M1 2l11 8 11-8" fill="none" stroke="#fff" stroke-width="2"/></svg></div>
  <div>Email:<br>info@tarvelrenovations<br>.com</div>
</div>

<div class="abs f-head" style="left:636px;top:4620px">GET A QUOTE</div>
<div class="abs field" style="left:636px;top:4676px">First Name</div>
<div class="abs field" style="left:636px;top:4726px">Email Address</div>
<div class="abs field" style="left:636px;top:4776px">Phone Number</div>
<div class="abs field" style="left:636px;top:4826px;height:72px">Message</div>
<div class="abs" style="left:770px;top:4910px;width:159px;height:38px;background:var(--green);color:#fff;font-size:13px;font-weight:600;text-align:center;line-height:38px">SUBMIT</div>

<div class="abs f-head" style="left:974px;top:4620px">QUICK LINKS</div>
<ul class="abs links" style="left:974px;top:4662px">
  <li>Home</li><li>Who We Are</li><li>Services Offered</li><li>Why Us</li><li>Recent Projects</li><li>Contact Us</li>
</ul>

<div class="abs" style="left:98px;top:4988px;width:1002px;height:1px;background:#444"></div>
<div class="abs center copy">&copy;Copyright &copy;2022 Tarvel Renovations And Custom Builds. All Rights Reserved.</div>

</body>
</html>
```